QR TILL WORKS , CREDIT CARD PROCESSING EQUIPMENT

qrtillworks is a sub division of Tallow a credit car processing co.
oren maddock
14 cedar hollow ln
Elmbrook OH 07312
suite 412

qrtillworks.example
cell 555-214-7730
office 555-861-2093
we sell pos systems to merchant who want to accept credit cards at there retail location.
black card would be nice buit open to different ideas

Target Market(s)

retail merchants

Industry/Entity Type

credit card processing

Contact Information for Business Card

card should include web site phone address

Colors

Designer to choose colors to be used in the design.

Requirements
Should not have
• red

```html
<!DOCTYPE html>
<html lang="en">
<head>
<meta charset="utf-8">
<title>QR TILL WORKS – Business Card</title>
<link rel="stylesheet" href="https://fonts.googleapis.com/css2?family=Open+Sans:wght@600;700&display=swap">
<style>
  :root {
    --backdrop: #a9a9a9;
    --card: #080808;
    --ink: #ffffff;
    --accent: #e6bd16;
    --tag-text: #0a0a0a;
  }
  html, body {
    margin: 0;
    padding: 0;
    width: 1127px;
    height: 1200px;
    overflow: hidden;
    background: var(--backdrop);
    font-family: "Open Sans", Arial, sans-serif;
  }
  .canvas {
    position: relative;
    width: 1127px;
    height: 1200px;
  }
  .card {
    position: absolute;
    left: 323px;
    width: 514px;
    height: 296px;
    background: var(--card);
    overflow: hidden;
  }
  .card-front { top: 264px; }
  .card-back { top: 642px; }

  /* Front: wordmark */
  .wordmark {
    position: absolute;
    inset: 0;
    display: flex;
    align-items: center;
    justify-content: center;
    gap: 14px;
  }
  .wordmark-dot {
    width: 22px;
    height: 22px;
    border-radius: 50%;
    background: var(--accent);
  }
  .wordmark-name {
    color: var(--ink);
    font-weight: 700;
    font-size: 40px;
    letter-spacing: 1px;
    line-height: 1;
  }

  /* Back: contact side */
  .holder-name {
    position: absolute;
    left: 41px;
    top: 42px;
    margin: 0;
    font-weight: 700;
    font-size: 33px;
    line-height: 44px;
  }
  .holder-first { display: block; color: var(--ink); }
  .holder-last { display: block; color: var(--accent); }

  .website-tag {
    position: absolute;
    left: 41px;
    top: 228px;
    height: 23px;
    padding: 0 8px;
    background: var(--accent);
    color: var(--tag-text);
    font-weight: 600;
    font-size: 15px;
    line-height: 23px;
    letter-spacing: 0.6px;
  }

  .address {
    position: absolute;
    left: 290px;
    top: 52px;
    display: flex;
    gap: 8px;
    font-style: normal;
  }
  .address-lines {
    color: var(--ink);
    font-weight: 600;
    font-size: 14px;
    line-height: 19px;
    letter-spacing: 1.4px;
  }
  .address-lines span { display: block; }

  .phones {
    position: absolute;
    left: 290px;
    top: 206px;
    margin: 0;
    padding: 0;
    list-style: none;
  }
  .phones li {
    display: flex;
    align-items: center;
    gap: 8px;
    color: var(--ink);
    font-weight: 600;
    font-size: 16.5px;
    line-height: 26px;
    letter-spacing: 1.5px;
  }
  .icon { width: 15px; height: 15px; flex: none; }
  .icon-pin { margin-top: 2px; }

  .corner-accent {
    position: absolute;
    right: 0;
    bottom: 0;
    width: 110px;
    height: 86px;
  }
</style>
</head>
<body>
<main class="canvas">

  <section class="card card-front" aria-label="Card front">
    <div class="wordmark">
      <span class="wordmark-dot"></span>
      <span class="wordmark-name">QR TILL WORKS</span>
    </div>
  </section>

  <section class="card card-back" aria-label="Card back">
    <h1 class="holder-name">
      <span class="holder-first">oren</span>
      <span class="holder-last">maddock</span>
    </h1>

    <address class="address">
      <svg class="icon icon-pin" viewBox="0 0 16 16" aria-hidden="true">
        <path d="M8 0.5a5.5 5.5 0 0 0-5.5 5.5c0 4 5.5 9.5 5.5 9.5s5.5-5.5 5.5-9.5A5.5 5.5 0 0 0 8 0.5z" fill="var(--accent)"/>
        <circle cx="8" cy="6" r="2.2" fill="var(--card)"/>
      </svg>
      <span class="address-lines">
        <span>14 Cedar Hollow Ln</span>
        <span>Elmbrook OH 07312</span>
        <span>Suite 412</span>
      </span>
    </address>

    <ul class="phones">
      <li>
        <svg class="icon" viewBox="0 0 16 16" aria-hidden="true">
          <rect x="3.5" y="0.8" width="9" height="14.4" rx="1.6" fill="none" stroke="var(--accent)" stroke-width="1.6"/>
          <rect x="6.5" y="12" width="3" height="1.2" fill="var(--accent)"/>
        </svg>
        <span>555-214-7730</span>
      </li>
      <li>
        <svg class="icon" viewBox="0 0 16 16" aria-hidden="true">
          <path d="M1 6c0-2.5 3.5-3.5 7-3.5s7 1 7 3.5v1.2h-3.4V5.6c-1-.5-2.3-.7-3.6-.7s-2.6.2-3.6.7v1.6H1z" fill="var(--accent)"/>
          <path d="M4.5 8h7l2 5.5h-11z" fill="var(--accent)"/>
          <circle cx="8" cy="10.5" r="1.5" fill="var(--card)"/>
        </svg>
        <span>555-861-2093</span>
      </li>
    </ul>

    <div class="website-tag">qrtillworks.example</div>

    <svg class="corner-accent" viewBox="0 0 110 86" aria-hidden="true">
      <polygon points="110,0 110,86 0,86" fill="var(--accent)"/>
    </svg>
  </section>

</main>
</body>
</html>
```